This is for a poster that will be hanging in the window of a Men's Suit Store in the mall:
Size 4 feet wide by 6 feet high
Main point is: A sale on "Suits" or "Men's Suits" at 40%-60% off ( the 40%-60% off should be the focal point)
Some words that can be used are "Sale" or "Clearance Sale"
Some key words that can be used to make it urgent are "limited time offer" or something similar.
You can get creative, the point is for the customer to want to come into the store and buy a suit right away.
You may use a graphic (picture of a man in a suit). It is not necessary but if it looks good you can use it. (If you do use a picture, it should be of a modern fit or slim fit suit)
Sorry, the initial brief somehow got deleted from the project. Please see the updated brief.
Thanks
Reason: Project was closed for some reason, extended to give enough time to complete
Target Market(s)
Mostly Men ages 35-55
Industry/Entity Type
Store
Colors
Designer to choose colors to be used in the design.

```html
<!DOCTYPE html>
<html lang="en">
<head>
<meta charset="utf-8">
<title>Suits Clearance Sale – Window Poster</title>
<link rel="stylesheet" href="https://fonts.googleapis.com/css2?family=Anton&family=Montserrat:wght@300;400;600;800&display=swap">
<style>
  :root {
    --page: #ffffff;
    --red-deep: #7a1307;
    --red-mid: #9c2210;
    --red-warm: #b5472a;
    --ink-white: #f7f7f7;
    --shadow: rgba(40, 4, 0, 0.55);
    --curl-light: #f4f4f4;
    --curl-dark: #8d8d8d;
  }
  html, body {
    margin: 0;
    padding: 0;
    width: 1200px;
    height: 860px;
    overflow: hidden;
    background: var(--page);
  }
  .board {
    position: relative;
    width: 1200px;
    height: 860px;
  }
  .poster {
    position: absolute;
    top: 44px;
    width: 514px;
    height: 769px;
    box-shadow: 0 2px 6px rgba(0,0,0,0.25);
  }
  .poster--photo { left: 35px; }
  .poster--plain { left: 651px; }
  .poster svg { display: block; width: 100%; height: 100%; }
  .headline {
    fill: var(--ink-white);
    filter: drop-shadow(2px 3px 2px var(--shadow));
  }
  .word-suits { font-family: "Montserrat", sans-serif; font-weight: 800; }
  .word-discount, .word-off, .word-sale { font-family: "Anton", sans-serif; }
  .word-clearance { font-family: "Montserrat", sans-serif; font-weight: 400; }
  .word-offer { font-family: "Montserrat", sans-serif; font-weight: 600; }
</style>
</head>
<body>
<div class="board">

  <!-- Poster variant with model background -->
  <div class="poster poster--photo">
    <svg viewBox="0 0 492 736" xmlns="http://www.w3.org/2000/svg">
      <defs>
        <linearGradient id="bgA" x1="0" y1="1" x2="1" y2="0">
          <stop offset="0" stop-color="#c05433"/>
          <stop offset="0.45" stop-color="#9c2210"/>
          <stop offset="1" stop-color="#7a1307"/>
        </linearGradient>
        <linearGradient id="modelA" x1="0" y1="0" x2="0" y2="1">
          <stop offset="0" stop-color="#6e1206" stop-opacity="0.75"/>
          <stop offset="1" stop-color="#8f1c0b" stop-opacity="0.15"/>
        </linearGradient>
        <linearGradient id="curlA" x1="0" y1="0" x2="0" y2="1">
          <stop offset="0" stop-color="#6b6b6b"/>
          <stop offset="0.35" stop-color="#f4f4f4"/>
          <stop offset="0.7" stop-color="#e2e2e2"/>
          <stop offset="1" stop-color="#7d7d7d"/>
        </linearGradient>
        <linearGradient id="footA" x1="0" y1="0" x2="1" y2="0">
          <stop offset="0" stop-color="#b5472a"/>
          <stop offset="1" stop-color="#8e1e0d"/>
        </linearGradient>
      </defs>
      <rect class="bg" width="492" height="736" fill="url(#bgA)"/>
      <path class="model-photo" role="img" aria-label="Photo of a man in a slim-fit dark suit, faded into the red background"
            d="M150 0 H360 L380 60 L470 110 L475 620 H40 L40 140 L120 80 Z" fill="url(#modelA)"/>
      <text class="headline word-suits" x="45" y="73" font-size="72" textLength="425" lengthAdjust="spacing">SUITS</text>
      <text class="headline word-discount" x="30" y="228" font-size="168" textLength="352" lengthAdjust="spacingAndGlyphs">40-60%</text>
      <text class="headline word-off" transform="translate(470 228) rotate(-90)" x="0" y="0" font-size="100" textLength="135" lengthAdjust="spacingAndGlyphs">OFF</text>
      <text class="headline word-clearance" x="30" y="298" font-size="52" textLength="440" lengthAdjust="spacing">CLEARANCE</text>
      <text class="headline word-sale" x="22" y="600" font-size="340" textLength="448" lengthAdjust="spacingAndGlyphs">SALE</text>
      <polygon class="curl-shadow" points="0,628 492,592 492,600 0,640" fill="#3a0702" opacity="0.5"/>
      <polygon class="page-curl" points="0,630 492,592 492,658 0,658" fill="url(#curlA)"/>
      <rect class="footer-band" x="0" y="658" width="492" height="78" fill="url(#footA)"/>
      <text class="headline word-offer" x="32" y="715" font-size="40" textLength="430" lengthAdjust="spacingAndGlyphs">Limited Time Offer</text>
    </svg>
  </div>

  <!-- Poster variant, plain background -->
  <div class="poster poster--plain">
    <svg viewBox="0 0 492 736" xmlns="http://www.w3.org/2000/svg">
      <defs>
        <linearGradient id="bgB" x1="0" y1="1" x2="1" y2="0">
          <stop offset="0" stop-color="#c05433"/>
          <stop offset="0.45" stop-color="#a2240f"/>
          <stop offset="1" stop-color="#7a1307"/>
        </linearGradient>
        <linearGradient id="curlB" x1="0" y1="0" x2="0" y2="1">
          <stop offset="0" stop-color="#6b6b6b"/>
          <stop offset="0.35" stop-color="#f4f4f4"/>
          <stop offset="0.7" stop-color="#e2e2e2"/>
          <stop offset="1" stop-color="#7d7d7d"/>
        </linearGradient>
        <linearGradient id="footB" x1="0" y1="0" x2="1" y2="0">
          <stop offset="0" stop-color="#b5472a"/>
          <stop offset="1" stop-color="#8e1e0d"/>
        </linearGradient>
      </defs>
      <rect class="bg" width="492" height="736" fill="url(#bgB)"/>
      <text class="headline word-suits" x="45" y="73" font-size="72" textLength="425" lengthAdjust="spacing">SUITS</text>
      <text class="headline word-discount" x="30" y="228" font-size="168" textLength="352" lengthAdjust="spacingAndGlyphs">40-60%</text>
      <text class="headline word-off" transform="translate(470 228) rotate(-90)" x="0" y="0" font-size="100" textLength="135" lengthAdjust="spacingAndGlyphs">OFF</text>
      <text class="headline word-clearance" x="30" y="298" font-size="52" textLength="440" lengthAdjust="spacing">CLEARANCE</text>
      <text class="headline word-sale" x="22" y="600" font-size="340" textLength="448" lengthAdjust="spacingAndGlyphs">SALE</text>
      <polygon class="curl-shadow" points="0,628 492,592 492,600 0,640" fill="#3a0702" opacity="0.5"/>
      <polygon class="page-curl" points="0,630 492,592 492,658 0,658" fill="url(#curlB)"/>
      <rect class="footer-band" x="0" y="658" width="492" height="78" fill="url(#footB)"/>
      <text class="headline word-offer" x="32" y="715" font-size="40" textLength="430" lengthAdjust="spacingAndGlyphs">Limited Time Offer</text>
    </svg>
  </div>

</div>
</body>
</html>
```